The Pixel Tap Business card.

A Simple card with our Logo and contact information. To give to investors and other professionals.

We are a nerd themed bar.
our target market is young professionals age 21+ but the real purpose of this business card is to present to potential investors and other professionals with our contact information. as we are still looking for funding before we start up.

I am partial to green and my partner likes red we are open to iteration.

Target Market(s)

Investors

Industry/Entity Type

Business

Contact Information for Business Card

Martin Hale (225) 730-6192 kent.h4711@mailnest.test Glen Porter (225) 968-5037 glenp318@mailnest.test

Font styles to use
Serif

Requirements
Nice to have
• Keep it simple but not boring.
• Use the Logos but feel free to edit them to match theme/colors.
• Keep the back clean and use one of the Logos.

```html
<!DOCTYPE html>
<html lang="en">
<head>
<meta charset="utf-8">
<title>The Pixel Tap – Business Card</title>
<link rel="stylesheet" href="https://fonts.googleapis.com/css2?family=Crimson+Text:wght@400;600;700&display=swap">
<style>
  :root {
    --page: #e8e5e0;
    --card-white: #f7f7f5;
    --card-black: #0b0b0b;
    --accent-red: #e0232e;
    --ink-dark: #111111;
    --ink-light: #f2f2f2;
    --divider: #6a6a6a;
  }
  * { box-sizing: border-box; margin: 0; padding: 0; }
  html, body {
    width: 1200px;
    height: 780px;
    overflow: hidden;
    background: var(--page);
    font-family: "Crimson Text", Georgia, serif;
  }
  .stage {
    position: relative;
    width: 1200px;
    height: 780px;
    display: flex;
    align-items: center;
    justify-content: center;
    gap: 50px;
  }
  .card {
    width: 525px;
    height: 300px;
    box-shadow: 0 6px 18px rgba(0,0,0,0.18);
    overflow: hidden;
    position: relative;
  }

  /* Front */
  .card-front {
    display: flex;
    flex-direction: column;
    background: var(--card-black);
  }
  .front-brand {
    height: 160px;
    background: var(--card-white);
    display: flex;
    flex-direction: column;
    align-items: center;
    justify-content: center;
    gap: 4px;
  }
  .brand-lockup {
    display: flex;
    align-items: center;
    gap: 12px;
  }
  .brand-dot {
    width: 22px;
    height: 22px;
    border-radius: 50%;
    background: var(--accent-red);
  }
  .brand-name {
    font-size: 44px;
    font-weight: 700;
    letter-spacing: 2px;
    text-transform: uppercase;
    color: var(--ink-dark);
    line-height: 1;
  }
  .brand-tagline {
    font-size: 14px;
    font-weight: 600;
    letter-spacing: 2.5px;
    text-transform: uppercase;
    color: var(--ink-dark);
  }
  .front-band {
    height: 9px;
    background: var(--accent-red);
  }
  .front-contacts {
    flex: 1;
    display: flex;
    align-items: center;
    justify-content: center;
    color: var(--ink-light);
  }
  .contact {
    padding: 0 22px;
    display: flex;
    flex-direction: column;
    gap: 1px;
  }
  .contact + .contact { border-left: 1px solid var(--divider); }
  .contact-name { font-size: 22px; font-weight: 600; line-height: 1.15; }
  .contact-line {
    display: flex;
    align-items: center;
    gap: 7px;
    font-size: 15px;
    line-height: 1.35;
  }
  .contact-icon {
    width: 13px;
    height: 13px;
    flex: none;
  }

  /* Back */
  .card-back {
    background: var(--card-black);
    display: flex;
    align-items: center;
    justify-content: center;
  }
  .back-lockup {
    display: flex;
    align-items: center;
    gap: 16px;
  }
  .back-lockup .brand-dot { width: 30px; height: 30px; }
  .back-lockup .brand-name {
    color: var(--ink-light);
    font-size: 56px;
  }
</style>
</head>
<body>
<main class="stage">

  <section class="card card-front" aria-label="Business card front">
    <div class="front-brand">
      <div class="brand-lockup">
        <span class="brand-dot"></span>
        <span class="brand-name">The Pixel Tap</span>
      </div>
      <p class="brand-tagline">Lounge and Arcade</p>
    </div>
    <div class="front-band"></div>
    <div class="front-contacts">
      <div class="contact">
        <p class="contact-name">Martin Hale</p>
        <p class="contact-line">(225) 730-6192
          <svg class="contact-icon" viewBox="0 0 16 16" aria-hidden="true"><rect width="16" height="16" rx="2" fill="#f2f2f2"/><path d="M4.5 3.5l2 1.5-1 2c.8 1.6 2 2.8 3.5 3.5l2-1 1.5 2-1.5 1.5C7.5 12.5 3.5 8.5 3 5z" fill="#0b0b0b"/></svg>
        </p>
        <p class="contact-line">kent.h4711@mailnest.test
          <svg class="contact-icon" viewBox="0 0 16 16" aria-hidden="true"><rect width="16" height="16" rx="2" fill="#f2f2f2"/><rect x="3" y="4.5" width="10" height="7" fill="none" stroke="#0b0b0b" stroke-width="1.3"/><path d="M3 4.5l5 4 5-4" fill="none" stroke="#0b0b0b" stroke-width="1.3"/></svg>
        </p>
      </div>
      <div class="contact">
        <p class="contact-name">Glen Porter</p>
        <p class="contact-line">(225) 968-5037
          <svg class="contact-icon" viewBox="0 0 16 16" aria-hidden="true"><rect width="16" height="16" rx="2" fill="#f2f2f2"/><path d="M4.5 3.5l2 1.5-1 2c.8 1.6 2 2.8 3.5 3.5l2-1 1.5 2-1.5 1.5C7.5 12.5 3.5 8.5 3 5z" fill="#0b0b0b"/></svg>
        </p>
        <p class="contact-line">glenp318@mailnest.test
          <svg class="contact-icon" viewBox="0 0 16 16" aria-hidden="true"><rect width="16" height="16" rx="2" fill="#f2f2f2"/><rect x="3" y="4.5" width="10" height="7" fill="none" stroke="#0b0b0b" stroke-width="1.3"/><path d="M3 4.5l5 4 5-4" fill="none" stroke="#0b0b0b" stroke-width="1.3"/></svg>
        </p>
      </div>
    </div>
  </section>

  <section class="card card-back" aria-label="Business card back">
    <div class="back-lockup">
      <span class="brand-dot"></span>
      <span class="brand-name">The Pixel Tap</span>
    </div>
  </section>

</main>
</body>
</html>
```